Computer tuition business needs Business card and Advertising Flyer

I am starting up a new business "Derek Halloway Computer Services" (DHCS for short) based in the Manning Valley NSW Australia.
The primary focus is on tuition\advice to the elderly and less computer literate in the region.
I will not be providing any repair services.

I have the line "At your home, On your computer, Answering your questions" in my head

I will need a Business card design (one sided) and Advertising Flyer design (A4 size, grayscale ).

Contact details on all these are - Mobile: 0412-583-906
- Email : dhalloway.pcservices@brindlemail.example

Target Market(s)

The primary focus is on tuition\advice to the elderly and less computer literate in the Manning Valley region of

Industry/Entity Type

Computer

```html
<!DOCTYPE html>
<html lang="en">
<head>
<meta charset="utf-8">
<title>DHCS Flyer</title>
<link rel="stylesheet" href="https://fonts.googleapis.com/css2?family=Questrial&family=Marcellus+SC&family=Archivo+Black&display=swap">
<style>
  :root {
    --stage: #e9e9e9;
    --paper: #ffffff;
    --ink: #111111;
    --ink-soft: #2b2b2b;
    --art-light: #f4f4f4;
    --art-dark: #cfcfcf;
  }
  * { box-sizing: border-box; margin: 0; padding: 0; }
  html, body {
    width: 1200px; height: 774px; overflow: hidden;
    background: var(--stage);
  }
  .flyer {
    position: absolute; left: 372px; top: 37px;
    width: 455px; height: 700px;
    background: var(--paper);
    overflow: hidden;
    box-shadow: 0 4px 18px rgba(0,0,0,0.18);
    font-family: "Questrial", "Century Gothic", sans-serif;
    color: var(--ink);
  }
  .brand {
    position: absolute; left: 0; right: 0; top: 62px;
    text-align: center;
    font-size: 72px; letter-spacing: 6px;
    color: var(--ink);
  }
  .banner-tab {
    position: absolute; width: 60px; height: 22px;
  }
  .banner-tab--top { left: 22px; top: 224px; }
  .banner-tab--bottom { left: 375px; top: 292px; }
  .banner {
    position: absolute; left: 16px; top: 241px;
    width: 424px; height: 54px;
    background: var(--ink); color: var(--paper);
    display: flex; align-items: center; justify-content: center;
    font-family: "Marcellus SC", "Copperplate", serif;
    font-size: 20px; letter-spacing: 1.2px;
  }
  .promises { position: absolute; left: 16px; top: 322px; list-style: none; }
  .promise {
    display: flex; align-items: center;
    height: 36px; margin-bottom: 27px;
    font-size: 29px; letter-spacing: 0.6px; color: var(--ink-soft);
  }
  .promise::before {
    content: ""; width: 31px; height: 31px; border-radius: 50%;
    background: var(--ink); margin-right: 9px; flex: none;
  }
  .tutor-art {
    position: absolute; left: 16px; top: 500px;
    width: 240px; height: 188px;
    background: radial-gradient(ellipse at 50% 50%, var(--art-light), var(--art-dark));
  }
  .call-corner { position: absolute; left: 0; top: 0; }
  .call {
    position: absolute; left: 262px; top: 584px;
    width: 220px; height: 52px;
    color: var(--paper);
    transform: rotate(-38deg); transform-origin: 50% 50%;
    text-align: center; line-height: 1.25;
  }
  .call__label { font-size: 18px; letter-spacing: 1px; padding-right: 40px; }
  .call__number {
    font-family: "Archivo Black", "Arial Black", sans-serif;
    font-size: 18px; letter-spacing: 1.2px;
  }
</style>
</head>
<body>
  <main class="flyer">
    <div class="brand">DHCS</div>

    <svg class="banner-tab banner-tab--top" viewBox="0 0 60 22" aria-hidden="true">
      <polygon points="0,22 60,0 60,22" fill="#111111"/>
    </svg>
    <div class="banner">Derek Halloway Computer Services</div>
    <svg class="banner-tab banner-tab--bottom" viewBox="0 0 60 22" aria-hidden="true">
      <polygon points="0,0 60,0 0,22" fill="#111111"/>
    </svg>

    <ul class="promises">
      <li class="promise">At your home.</li>
      <li class="promise">On your computer.</li>
      <li class="promise">Answering your questions.</li>
    </ul>

    <div class="tutor-art" role="img" aria-label="Line drawing of an older man sitting at a desktop computer with keyboard and mouse"></div>

    <svg class="call-corner" width="455" height="700" viewBox="0 0 455 700" aria-hidden="true">
      <path d="M286 700 C300 600 370 520 455 498 L455 700 Z" fill="#111111"/>
    </svg>
    <div class="call">
      <div class="call__label">Call Now</div>
      <div class="call__number">0412-583-906</div>
    </div>
  </main>
</body>
</html>
```